Waste management company seeks a new website design

We need a website design for an environmental services company called 'Rannamõisa Jäätmehooldus.' We manage waste collection and recycling for 100K+ households and businesses across Estonia. Please use logos and colors from attached CVI file. The design should be extensively usable for our self-service portal and have a mobile-first approach as it will be turned into an app in the future. The new website should highlight our commitment to sustainability and provide easy access to our services with a clean, modern design. UX inspiration from https://vorrix.eu/et-ee/

```html
<!DOCTYPE html>
<html lang="en">
<head>
<meta charset="utf-8">
<title>Rannamõisa Jäätmehooldus – Home page</title>
<link href="https://fonts.googleapis.com/css2?family=Poppins:wght@500;600;700&family=Roboto:wght@400;500;700&display=swap" rel="stylesheet">
<style>
:root{
  --lime:#cbdb2a;
  --lime-deep:#a9b81a;
  --brown:#7b6f63;
  --ink:#1f1f1f;
  --muted:#6b6b6b;
  --white:#ffffff;
  --canvas:#e4e4e4;
}
*{box-sizing:border-box;margin:0;padding:0}
html,body{width:881px;height:1200px;overflow:hidden}
body{background:var(--canvas);position:relative;font-family:"Roboto",sans-serif;color:var(--ink)}
.page{position:absolute;top:53px;width:668px;transform-origin:0 0;transform:scale(0.5333);overflow:hidden;background:var(--white)}
.page--tabs{left:53px;height:1719px}
.page--cards{left:472px;height:2052px}
.abs{position:absolute}
.page-bg{position:absolute;left:0;top:0;width:668px}
.photo{position:absolute}
.hero-photo{left:0;top:0;width:668px;height:470px;background:linear-gradient(180deg,#aebbc6 0%,#d6d2c6 30%,#d8c6a6 52%,#a69072 75%,#6c5f47 100%)}
/* nav */
.brand{display:flex;align-items:center;gap:5px}
.brand-dot{width:22px;height:22px;border-radius:50%;background:var(--brown);flex:none}
.brand-name{font-family:"Poppins",sans-serif;font-weight:500;font-size:9px;line-height:10px;color:var(--brown)}
.nav{left:80px;top:13px;width:508px;height:24px}
.nav-links{position:absolute;right:0;top:4px;display:flex;align-items:center;gap:18px;font-size:7px;color:var(--ink)}
.lang{display:flex;align-items:center;gap:3px}
.flag{width:6px;height:6px;border-radius:50%;background:#d23a2f}
.login{background:var(--lime);border-radius:9px;padding:4px 12px;font-weight:500}
.menu{width:8px;height:6px;border-top:1.2px solid var(--ink);border-bottom:1.2px solid var(--ink);position:relative}
.menu::after{content:"";position:absolute;left:0;right:0;top:1.2px;border-top:1.2px solid var(--ink)}
/* hero */
.hero-title{left:0;width:668px;top:114px;text-align:center;font-family:"Poppins",sans-serif;font-weight:600;font-size:22px;color:var(--ink)}
.hero-sub{left:184px;width:300px;top:150px;text-align:center;font-size:8.3px;line-height:13px;color:#3c3a36}
.btn{display:flex;align-items:center;justify-content:center;gap:4px;border-radius:12px;font-size:7.5px;font-weight:700;text-transform:uppercase;color:var(--ink);background:var(--lime)}
.btn-arrow{width:7px;height:7px;border-radius:50%;background:var(--ink);position:relative}
.btn-arrow::after{content:"";position:absolute;left:1.6px;top:2.1px;width:2px;height:2px;border-top:1px solid var(--lime);border-right:1px solid var(--lime);transform:rotate(45deg)}
.hero-btn{left:284px;top:190px;width:100px;height:24px}
.slide-arrow{top:158px;width:22px;height:22px;border-radius:50%;background:rgba(40,38,34,.55);border:1px solid rgba(255,255,255,.8)}
.slide-arrow::after{content:"";position:absolute;top:7px;width:6px;height:6px;border-top:1.4px solid #fff;border-right:1.4px solid #fff}
.slide-arrow.prev::after{left:9px;transform:rotate(-135deg)}
.slide-arrow.next::after{left:6px;transform:rotate(45deg)}
/* headings */
.section-title{font-family:"Poppins",sans-serif;font-weight:600;font-size:19px;color:var(--brown)}
.section-title .accent{color:var(--lime)}
.center-title{text-align:center;font-family:"Poppins",sans-serif;font-weight:600;font-size:17px}
.body-text{font-size:7px;line-height:13.5px;color:var(--muted);text-align:justify}
.body-text p+p{margin-top:7px}
/* about */
.about-photo{left:88px;top:385px;width:215px;height:205px;border-radius:50%;background:radial-gradient(circle at 35% 35%,#a9a49a 0%,#8f8a80 45%,#b7c944 72%,#8ea22a 100%)}
/* services */
.tab{top:720px;height:24px;border-radius:12px;display:flex;align-items:center;gap:7px;padding-left:4px;font-size:7.8px;font-weight:500;color:var(--ink)}
.tab-icon{width:17px;height:17px;border-radius:50%;background:#e9e6e0}
.tab--business{left:207px;width:121px;background:var(--lime)}
.tab--business::after{content:"";position:absolute;left:55px;bottom:-5px;border:5px solid transparent;border-bottom:0;border-top-color:var(--lime)}
.tab--private{left:341px;width:120px;background:var(--white)}
.tab--private .tab-icon{background:#8d837a}
.biz-heading{left:80px;top:780px;width:215px;font-family:"Poppins",sans-serif;font-weight:600;font-size:14.5px;line-height:19px;color:var(--white)}
.biz-list{left:80px;top:828px;list-style:none;font-size:7px;color:var(--white)}
.biz-list li{height:17px;display:flex;align-items:center;gap:5px}
.biz-list li::before{content:"";width:6px;height:6px;border-radius:50%;background:var(--white)}
.biz-photo{left:312px;top:771px;width:276px;height:179px;border-radius:14px;background:linear-gradient(135deg,#3d4a52 0%,#6c7780 35%,#8a8f88 60%,#3a3f38 100%)}
.svc-card{width:244px;height:90px;background:var(--white);border-radius:6px}
.svc-icon{position:absolute;left:14px;top:14px;width:36px;height:36px}
.svc-title{position:absolute;left:60px;top:16px;font-size:8px;font-weight:500;color:var(--ink)}
.svc-text{position:absolute;left:60px;top:33px;width:168px;font-size:6.5px;line-height:12px;color:var(--muted)}
.read-more{font-size:6.5px;font-weight:700;color:var(--lime);text-transform:uppercase;display:flex;align-items:center;gap:3px}
.read-more .btn-arrow{width:6px;height:6px;background:var(--lime)}
.read-more .btn-arrow::after{border-color:var(--white);left:1.2px;top:1.7px;width:1.8px;height:1.8px}
.svc-card .read-more{position:absolute;left:60px;top:66px}
/* environment */
.env-heading{left:80px;top:1072px;width:260px;font-family:"Poppins",sans-serif;font-weight:700;font-size:17.5px;line-height:20px;color:var(--brown);text-transform:uppercase}
.env-heading .accent{color:var(--lime)}
.env-photo{left:354px;top:1070px;width:234px;height:206px;border-radius:18px;background:radial-gradient(circle at 50% 55%,#b8d49a 0%,#4e8a3a 35%,#2e6a2a 65%,#1f4d22 100%)}
/* trust */
.trust-title{font-family:"Poppins",sans-serif;font-weight:600;font-size:18px;color:var(--ink);text-align:center}
.stat{width:130px;text-align:center}
.stat-ring{width:46px;height:46px;margin:0 auto;border-radius:50%;border:2px solid var(--white);display:flex;align-items:center;justify-content:center}
.stat-ring span{width:36px;height:36px;border-radius:50%;background:var(--white);display:flex;align-items:center;justify-content:center}
.stat-num{margin-top:11px;font-family:"Poppins",sans-serif;font-weight:600;font-size:12.5px;color:var(--ink)}
.stat-label{font-size:7px;color:#8f9840}
/* news */
.news-card{width:162px}
.news-photo{width:162px;height:111px;border-radius:8px}
.news-date{position:absolute;left:8px;top:104px;width:60px;height:14px;border-radius:7px;background:var(--lime);font-size:6px;display:flex;align-items:center;justify-content:center;gap:3px;color:var(--ink)}
.news-date::before{content:"";width:5px;height:5px;border:1px solid var(--ink);border-radius:1px}
.news-title{position:absolute;top:128px;left:0;width:150px;height:24px;display:flex;align-items:center;font-size:7.8px;line-height:11.5px;font-weight:500;color:var(--ink)}
.news-text{position:absolute;top:158px;left:0;width:158px;font-size:6.5px;line-height:11.5px;color:var(--muted)}
.news-card .read-more{position:absolute;top:190px;left:0}
.photo-1{background:linear-gradient(160deg,#4b3b2c 0%,#c39a66 45%,#e3c79a 70%,#8b7a66 100%)}
.photo-2{background:linear-gradient(160deg,#9ea476 0%,#d8c8a8 40%,#b89060 65%,#6f7a80 100%)}
.photo-3{background:linear-gradient(120deg,#2f6f6a 0%,#5fb0a0 30%,#c7a07a 60%,#3f4d3a 100%)}
/* footer */
.foot-brand .brand-dot{background:var(--lime)}
.foot-brand .brand-name{color:var(--lime);font-size:10px;line-height:11px}
.socials{display:flex;gap:7px}
.socials span{width:9px;height:9px;border-radius:50%;background:var(--white)}
.foot-head{font-size:8px;font-weight:500;color:var(--white)}
.contact{position:absolute;width:130px;font-size:6.5px;line-height:9px;color:var(--white);padding-left:12px}
.contact b{display:block;font-weight:700;font-size:6px}
.contact svg{position:absolute;left:0;top:1px;width:8px;height:8px}
.foot-list{list-style:none;font-size:6.8px;line-height:13.5px;color:var(--white)}
.foot-note{font-size:6.5px;line-height:9.5px;color:var(--white)}
.quote-btn{width:103px;height:21px;border-radius:11px;background:var(--white);font-size:7.5px;font-weight:700;color:var(--ink);display:flex;align-items:center;justify-content:center}
.foot-rule{left:80px;width:508px;height:0;border-top:1px solid rgba(255,255,255,.45)}
.go-up{width:42px;height:12px;border-radius:6px;background:#4a423a;font-size:5.5px;font-weight:700;color:var(--white);display:flex;align-items:center;justify-content:center}
.legal{font-size:6.5px;color:var(--white)}
.legal-links{display:flex;gap:5px}
</style>
</head>
<body>

<!-- ===================== Home page – tabbed services ===================== -->
<main class="page page--tabs">
  <div class="photo hero-photo" role="img" aria-label="Misty Estonian bog with pine trees and a wooden boardwalk at sunrise"></div>
  <svg class="page-bg" height="1719" viewBox="0 0 668 1719" aria-hidden="true">
    <path d="M0,418 C180,350 420,305 668,310 L668,660 L0,660Z" fill="#fff"/>
    <path d="M0,396 C180,330 420,292 668,298 L668,312 C420,308 180,352 0,424Z" fill="#cbdb2a"/>
    <path d="M0,655 C250,660 500,612 668,560 L668,990 L0,990Z" fill="#7b6f63"/>
    <path d="M0,642 C250,645 500,595 668,538 L668,562 C500,614 250,662 0,657Z" fill="#cbdb2a"/>
    <rect x="0" y="990" width="668" height="176" fill="#cbdb2a"/>
    <path d="M0,1526 C250,1526 500,1490 668,1440 L668,1719 L0,1719Z" fill="#7b6f63"/>
    <path d="M0,1510 C250,1512 500,1470 668,1418 L668,1442 C500,1492 250,1528 0,1528Z" fill="#cbdb2a"/>
  </svg>

  <header class="abs nav">
    <div class="brand"><span class="brand-dot"></span><span class="brand-name">Rannamõisa<br>Jäätmehooldus</span></div>
    <nav class="nav-links">
      <span class="lang"><span class="flag"></span>EN ▾</span>
      <span>Client Support</span>
      <span class="login">login</span>
      <span class="menu"></span>
    </nav>
  </header>

  <h1 class="abs hero-title">Rannamõisa Jäätmehooldus</h1>
  <p class="abs hero-sub">Rannamõisa Jäätmehooldus is Estonia's leading group providing waste management and communal services.</p>
  <a class="abs btn hero-btn">Get Started <span class="btn-arrow"></span></a>
  <span class="abs slide-arrow prev" style="left:40px"></span>
  <span class="abs slide-arrow next" style="left:606px"></span>

  <div class="photo about-photo" role="img" aria-label="Waste collection worker and green recycling containers"></div>
  <h2 class="abs section-title" style="left:345px;top:398px">About <span class="accent">Us</span></h2>
  <div class="abs body-text" style="left:345px;top:434px;width:243px">
    <p>Rannamõisa Jäätmehooldus is Estonia's leading group providing waste management and communal services, whose main activity is the collection of household waste. In addition, the company collects secondary raw materials, construction waste and other waste.</p>
    <p>In some areas, the company also offers road and street maintenance services during the winter. The company serves more than 100,000 customers in Estonia and handles over 250,000 tons of waste per year.</p>
  </div>
  <a class="abs btn" style="left:345px;top:552px;width:82px;height:20px">Read More <span class="btn-arrow"></span></a>

  <h2 class="abs center-title" style="left:0;width:668px;top:686px;color:#fff">OUR SERVICES</h2>
  <div class="abs tab tab--business"><span class="tab-icon"></span>Business Customers</div>
  <div class="abs tab tab--private"><span class="tab-icon"></span>Private Customers</div>

  <h3 class="abs biz-heading">SERVICES FOR BUSINESS CUSTOMERS</h3>
  <ul class="abs biz-list">
    <li>Hazardous waste and electronics</li>
    <li>Destruction of documents and goods</li>
    <li>Construction and cleaning waste</li>
    <li>Purchase of recyclable waste/materials</li>
    <li>Roads and streets</li>
    <li>Other services</li>
    <li>Big Bag</li>
  </ul>
  <div class="photo biz-photo" role="img" aria-label="Workers sorting electronic waste at an outdoor collection point"></div>

  <h2 class="abs trust-title" style="left:318px;width:200px;top:1020px">OUR TRUST</h2>
  <div class="abs stat" style="left:240px;top:1053px">
    <div class="stat-ring"><span><svg width="18" height="18" viewBox="0 0 24 24" fill="none" stroke="#7b6f63" stroke-width="1.4"><path d="M12 3l4 7H8z"/><path d="M4 20l4-7 4 7z"/><path d="M20 20l-4-7-4 7z"/></svg></span></div>
    <div class="stat-num">100K+</div><div class="stat-label">Waste Collection and Recycling</div>
  </div>
  <div class="abs stat" style="left:360px;top:1053px">
    <div class="stat-ring"><span><svg width="18" height="18" viewBox="0 0 24 24" fill="none" stroke="#7b6f63" stroke-width="1.4"><circle cx="12" cy="12" r="9"/><path d="M3 12h18M12 3c3 3 3 15 0 18M12 3c-3 3-3 15 0 18"/></svg></span></div>
    <div class="stat-num">5</div><div class="stat-label">45+ Countries</div>
  </div>
  <div class="abs stat" style="left:472px;top:1053px">
    <div class="stat-ring"><span><svg width="18" height="18" viewBox="0 0 24 24" fill="none" stroke="#7b6f63" stroke-width="1.4"><circle cx="8" cy="7" r="2.5"/><circle cx="16" cy="7" r="2.5"/><path d="M3 20c0-4 2-7 5-7s5 3 5 7M11 20c0-4 2-7 5-7s5 3 5 7"/></svg></span></div>
    <div class="stat-num">150+</div><div class="stat-label">Customers all over the world</div>
  </div>

  <h2 class="abs section-title" style="left:0;width:668px;top:1203px;text-align:center">LATEST <span class="accent">NEWS</span></h2>
  <article class="abs news-card" style="left:80px;top:1246px">
    <div class="news-photo photo-1" role="img" aria-label="Smiling woman in a knitted sweater in an autumn forest"></div>
    <span class="news-date">14.12.2023</span>
    <h4 class="news-title">Change of opening hours of Tallinn customer service</h4>
    <p class="news-text">From 01.01.2024, Tallinn's customer service is open Mon-Fri 9:00-17:00.</p>
    <a class="read-more">Read More <span class="btn-arrow"></span></a>
  </article>
  <article class="abs news-card" style="left:253px;top:1246px">
    <div class="news-photo photo-2" role="img" aria-label="Person holding a cardboard box of plastic bottles for recycling"></div>
    <span class="news-date">14.12.2023</span>
    <h4 class="news-title">VAT rate change from 01.01.2024</h4>
    <p class="news-text">From 01.01.2024, Tallinn's customer service is open Mon-Fri 9:00-17:00.</p>
    <a class="read-more">Read More <span class="btn-arrow"></span></a>
  </article>
  <article class="abs news-card" style="left:426px;top:1246px">
    <div class="news-photo photo-3" role="img" aria-label="Hand dropping a plastic bottle into a recycling bin"></div>
    <span class="news-date">14.12.2023</span>
    <h4 class="news-title">Invoicing changes</h4>
    <p class="news-text">From 01.01.2024, Tallinn's customer service is open Mon-Fri 9:00-17:00.</p>
    <a class="read-more">Read More <span class="btn-arrow"></span></a>
  </article>

  <footer>
    <div class="abs brand foot-brand" style="left:80px;top:1590px"><span class="brand-dot"></span><span class="brand-name">Rannamõisa<br>Jäätmehooldus</span></div>
    <div class="abs socials" style="left:112px;top:1629px"><span></span><span></span><span></span><span></span></div>
    <h5 class="abs foot-head" style="left:237px;top:1566px">Our Office Address</h5>
    <div class="contact" style="left:237px;top:1587px"><svg viewBox="0 0 24 24" fill="#fff"><path d="M6 3l4 4-2 3c1 3 3 5 6 6l3-2 4 4-3 3C10 21 3 14 3 6z"/></svg><b>Phone</b>(+372) 600 12 34</div>
    <div class="contact" style="left:237px;top:1614px"><svg viewBox="0 0 24 24" fill="#fff"><path d="M2 5h20v14H2z"/></svg><b>Email</b>info@rannamoisa.ee</div>
    <div class="contact" style="left:237px;top:1641px"><svg viewBox="0 0 24 24" fill="#fff"><path d="M12 2a7 7 0 0 0-7 7c0 5 7 13 7 13s7-8 7-13a7 7 0 0 0-7-7z"/></svg><b>Location</b>AS Rannamõisa Jäätmehooldus<br>Lepiku 8, Tallinn 10115</div>
    <h5 class="abs foot-head" style="left:373px;top:1566px">Company</h5>
    <ul class="abs foot-list" style="left:373px;top:1586px"><li>Home</li><li>Home customer</li><li>Business customer</li><li>Client support</li><li>About the company</li><li>Come to work!</li></ul>
    <h5 class="abs foot-head" style="left:470px;top:1566px">Still Have Questions?</h5>
    <p class="abs foot-note" style="left:470px;top:1588px;width:122px">Contact us using this form. A representative will answer your questions as soon as possible.</p>
    <a class="abs quote-btn" style="left:470px;top:1631px">GET A QUOTE</a>
    <div class="abs foot-rule" style="top:1680px"></div>
    <a class="abs go-up" style="left:546px;top:1674px">▲ Go Up</a>
    <p class="abs legal" style="left:80px;top:1697px">© 2024 rannamoisa | All Rights Reserved</p>
    <p class="abs legal legal-links" style="left:418px;top:1697px;width:170px;justify-content:flex-end"><span>Privacy Policy</span>|<span>Cookie Policy</span>|<span>Terms Of Services</span></p>
  </footer>
</main>

<!-- ===================== Home page – service cards ===================== -->
<main class="page page--cards">
  <div class="photo hero-photo" role="img" aria-label="Misty Estonian bog with pine trees and a wooden boardwalk at sunrise"></div>
  <svg class="page-bg" height="2052" viewBox="0 0 668 2052" aria-hidden="true">
    <path d="M0,418 C180,350 420,305 668,310 L668,660 L0,660Z" fill="#fff"/>
    <path d="M0,396 C180,330 420,292 668,298 L668,312 C420,308 180,352 0,424Z" fill="#cbdb2a"/>
    <path d="M0,655 C250,660 500,612 668,560 L668,1021 L0,1021Z" fill="#7b6f63"/>
    <path d="M0,642 C250,645 500,595 668,538 L668,562 C500,614 250,662 0,657Z" fill="#cbdb2a"/>
    <rect x="0" y="1322" width="668" height="178" fill="#cbdb2a"/>
    <path d="M0,1860 C250,1860 500,1824 668,1774 L668,2052 L0,2052Z" fill="#7b6f63"/>
    <path d="M0,1844 C250,1846 500,1804 668,1752 L668,1776 C500,1826 250,1862 0,1862Z" fill="#cbdb2a"/>
  </svg>

  <header class="abs nav">
    <div class="brand"><span class="brand-dot"></span><span class="brand-name">Rannamõisa<br>Jäätmehooldus</span></div>
    <nav class="nav-links">
      <span class="lang"><span class="flag"></span>EN ▾</span>
      <span>Client Support</span>
      <span class="login">login</span>
      <span class="menu"></span>
    </nav>
  </header>

  <h1 class="abs hero-title">Rannamõisa Jäätmehooldus</h1>
  <p class="abs hero-sub">Rannamõisa Jäätmehooldus is Estonia's leading group providing waste management and communal services.</p>
  <a class="abs btn hero-btn">Get Started <span class="btn-arrow"></span></a>
  <span class="abs slide-arrow prev" style="left:40px"></span>
  <span class="abs slide-arrow next" style="left:606px"></span>

  <div class="photo about-photo" role="img" aria-label="Waste collection truck and green recycling containers"></div>
  <h2 class="abs section-title" style="left:345px;top:398px">About <span class="accent">Us</span></h2>
  <div class="abs body-text" style="left:345px;top:434px;width:243px">
    <p>Rannamõisa Jäätmehooldus is Estonia's leading group providing waste management and communal services, whose main activity is the collection of household waste. In addition, the company collects secondary raw materials, construction waste and other waste.</p>
    <p>In some areas, the company also offers road and street maintenance services during the winter. The company serves more than 100,000 customers in Estonia and handles over 250,000 tons of waste per year.</p>
  </div>
  <a class="abs btn" style="left:345px;top:552px;width:82px;height:20px">Read More <span class="btn-arrow"></span></a>

  <h2 class="abs center-title" style="left:0;width:668px;top:686px;color:#fff">OUR SERVICES</h2>
  <div class="abs tab tab--business"><span class="tab-icon"></span>Business Customers</div>
  <div class="abs tab tab--private"><span class="tab-icon"></span>Private Customers</div>

  <article class="abs svc-card" style="left:80px;top:774px">
    <svg class="svc-icon" viewBox="0 0 36 36" fill="none" stroke="#7b6f63" stroke-width="1"><ellipse cx="14" cy="8" rx="9" ry="3"/><path d="M5 8v20c0 2 4 3 9 3s9-1 9-3V8"/><circle cx="14" cy="19" r="4" fill="#cbdb2a"/><path d="M26 22l6 10H20z" fill="#fff"/></svg>
    <h4 class="svc-title">Hazardous waste and electronics</h4>
    <p class="svc-text">In cooperation with the RJH group company AS Kallas &amp; Mets, we offer our customers</p>
    <a class="read-more">Read More <span class="btn-arrow"></span></a>
  </article>
  <article class="abs svc-card" style="left:342px;top:774px">
    <svg class="svc-icon" viewBox="0 0 36 36" fill="none" stroke="#7b6f63" stroke-width="1"><path d="M4 10l10-4 4 22-10 4z"/><path d="M12 4h16v26H12z" fill="#fff"/><path d="M16 10h8M16 14h8M16 18h8M16 22h5" stroke="#cbdb2a"/></svg>
    <h4 class="svc-title">Destruction of documents and goods</h4>
    <p class="svc-text">In cooperation with AS Kallas &amp; Mets, a company of the RJH group, we offer the service</p>
    <a class="read-more">Read More <span class="btn-arrow"></span></a>
  </article>
  <article class="abs svc-card" style="left:80px;top:882px">
    <svg class="svc-icon" viewBox="0 0 36 36" fill="none" stroke="#7b6f63" stroke-width="1"><path d="M4 6h26M8 6v26M8 10l6-4M14 6v6"/><path d="M4 32h28"/><path d="M14 20h8v12h-8zM24 16h6v16h-6z" fill="#cbdb2a" fill-opacity=".5"/></svg>
    <h4 class="svc-title">Construction and cleaning waste</h4>
    <p class="svc-text">The collection and transport of construction and cleaning waste is generally carried out with</p>
    <a class="read-more">Read More <span class="btn-arrow"></span></a>
  </article>
  <article class="abs svc-card" style="left:342px;top:882px">
    <svg class="svc-icon" viewBox="0 0 36 36" fill="none" stroke="#7b6f63" stroke-width="1"><path d="M8 14h20l-2 18H10z"/><path d="M6 14h24"/><path d="M12 14V4M17 14V6M22 14V3M26 14l2-8"/><path d="M15 26l3-5 3 5z" stroke="#cbdb2a"/></svg>
    <h4 class="svc-title">Purchase of recyclable waste</h4>
    <p class="svc-text">Waste recycling is a waste management operation by which waste or the substance or material</p>
    <a class="read-more">Read More <span class="btn-arrow"></span></a>
  </article>

  <h2 class="abs env-heading">Environment, Quality<br>and <span class="accent">Occupational<br>Safety</span></h2>
  <div class="abs body-text" style="left:80px;top:1146px;width:243px">
    <p>In our activities, we have tried to be completely modern, introduced new technologies and trained our team. We are flexible towards our customers and considerate of customer wishes, because pleasant cooperation and customer satisfaction guarantee our strength.</p>
    <p>Employees are actively involved in the development of the company's daily activities, in the development and implementation of strategies.</p>
  </div>
  <a class="abs btn" style="left:80px;top:1250px;width:82px;height:20px">Read More <span class="btn-arrow"></span></a>
  <div class="photo env-photo" role="img" aria-label="Aerial view of a dense green forest under light clouds"></div>

  <h2 class="abs trust-title" style="left:318px;width:200px;top:1354px">OUR TRUST</h2>
  <div class="abs stat" style="left:240px;top:1387px">
    <div class="stat-ring"><span><svg width="18" height="18" viewBox="0 0 24 24" fill="none" stroke="#7b6f63" stroke-width="1.4"><path d="M12 3l4 7H8z"/><path d="M4 20l4-7 4 7z"/><path d="M20 20l-4-7-4 7z"/></svg></span></div>
    <div class="stat-num">100K+</div><div class="stat-label">Waste Collection and Recycling</div>
  </div>
  <div class="abs stat" style="left:360px;top:1387px">
    <div class="stat-ring"><span><svg width="18" height="18" viewBox="0 0 24 24" fill="none" stroke="#7b6f63" stroke-width="1.4"><circle cx="12" cy="12" r="9"/><path d="M3 12h18M12 3c3 3 3 15 0 18M12 3c-3 3-3 15 0 18"/></svg></span></div>
    <div class="stat-num">5</div><div class="stat-label">45+ Countries</div>
  </div>
  <div class="abs stat" style="left:472px;top:1387px">
    <div class="stat-ring"><span><svg width="18" height="18" viewBox="0 0 24 24" fill="none" stroke="#7b6f63" stroke-width="1.4"><circle cx="8" cy="7" r="2.5"/><circle cx="16" cy="7" r="2.5"/><path d="M3 20c0-4 2-7 5-7s5 3 5 7M11 20c0-4 2-7 5-7s5 3 5 7"/></svg></span></div>
    <div class="stat-num">150+</div><div class="stat-label">Customers all over the world</div>
  </div>

  <h2 class="abs section-title" style="left:0;width:668px;top:1537px;text-align:center">LATEST <span class="accent">NEWS</span></h2>
  <article class="abs news-card" style="left:80px;top:1580px">
    <div class="news-photo photo-1" role="img" aria-label="Smiling woman in a knitted sweater in an autumn forest"></div>
    <span class="news-date">14.12.2023</span>
    <h4 class="news-title">Change of opening hours of Tallinn customer service</h4>
    <p class="news-text">From 01.01.2024, Tallinn's customer service is open Mon-Fri 9:00-17:00.</p>
    <a class="read-more">Read More <span class="btn-arrow"></span></a>
  </article>
  <article class="abs news-card" style="left:253px;top:1580px">
    <div class="news-photo photo-2" role="img" aria-label="Person holding a cardboard box of plastic bottles for recycling"></div>
    <span class="news-date">14.12.2023</span>
    <h4 class="news-title">VAT rate change from 01.01.2024</h4>
    <p class="news-text">From 01.01.2024, Tallinn's customer service is open Mon-Fri 9:00-17:00.</p>
    <a class="read-more">Read More <span class="btn-arrow"></span></a>
  </article>
  <article class="abs news-card" style="left:426px;top:1580px">
    <div class="news-photo photo-3" role="img" aria-label="Hand dropping a plastic bottle into a recycling bin"></div>
    <span class="news-date">14.12.2023</span>
    <h4 class="news-title">Invoicing changes</h4>
    <p class="news-text">From 01.01.2024, Tallinn's customer service is open Mon-Fri 9:00-17:00.</p>
    <a class="read-more">Read More <span class="btn-arrow"></span></a>
  </article>

  <footer>
    <div class="abs brand foot-brand" style="left:80px;top:1924px"><span class="brand-dot"></span><span class="brand-name">Rannamõisa<br>Jäätmehooldus</span></div>
    <div class="abs socials" style="left:112px;top:1963px"><span></span><span></span><span></span><span></span></div>
    <h5 class="abs foot-head" style="left:237px;top:1900px">Our Office Address</h5>
    <div class="contact" style="left:237px;top:1921px"><svg viewBox="0 0 24 24" fill="#fff"><path d="M6 3l4 4-2 3c1 3 3 5 6 6l3-2 4 4-3 3C10 21 3 14 3 6z"/></svg><b>Phone</b>(+372) 600 12 34</div>
    <div class="contact" style="left:237px;top:1948px"><svg viewBox="0 0 24 24" fill="#fff"><path d="M2 5h20v14H2z"/></svg><b>Email</b>info@rannamoisa.ee</div>
    <div class="contact" style="left:237px;top:1975px"><svg viewBox="0 0 24 24" fill="#fff"><path d="M12 2a7 7 0 0 0-7 7c0 5 7 13 7 13s7-8 7-13a7 7 0 0 0-7-7z"/></svg><b>Location</b>AS Rannamõisa Jäätmehooldus<br>Lepiku 8, Tallinn 10115</div>
    <h5 class="abs foot-head" style="left:373px;top:1900px">Company</h5>
    <ul class="abs foot-list" style="left:373px;top:1920px"><li>Home</li><li>Home customer</li><li>Business customer</li><li>Client support</li><li>About the company</li><li>Come to work!</li></ul>
    <h5 class="abs foot-head" style="left:470px;top:1900px">Still Have Questions?</h5>
    <p class="abs foot-note" style="left:470px;top:1922px;width:122px">Contact us using this form. A representative will answer your questions as soon as possible.</p>
    <a class="abs quote-btn" style="left:470px;top:1965px">GET A QUOTE</a>
    <div class="abs foot-rule" style="top:2014px"></div>
    <a class="abs go-up" style="left:546px;top:2008px">▲ Go Up</a>
    <p class="abs legal" style="left:80px;top:2031px">© 2024 rannamoisa | All Rights Reserved</p>
    <p class="abs legal legal-links" style="left:418px;top:2031px;width:170px;justify-content:flex-end"><span>Privacy Policy</span>|<span>Cookie Policy</span>|<span>Terms Of Services</span></p>
  </footer>
</main>

</body>
</html>
```